Business Card design, larkwell shipping

I started a container shipping company which specialized in export of cars, motorcycles, boats and general cargo overseas. I need a business card that stands out of the pack and gives clients an idea of what I do. I have attached a sample that someone designed for me but I don't think its the right fit. However the info on it is accurate so can be used right on new card.
Updates

Reason: I would like my new logo which is being designed on PLANOVISTRA.COM as well to be implemented into my business card.

Industry/Entity Type

Shipping

```html
<!DOCTYPE html>
<html lang="en">
<head>
<meta charset="utf-8">
<title>Larkwell Shipping – Business Card</title>
<link rel="stylesheet" href="https://fonts.googleapis.com/css2?family=Questrial&family=Tinos:wght@700&display=swap">
<style>
  :root {
    --brand-blue: #1c9ae0;
    --card-blue: #1592dc;
    --navy: #27294f;
    --ink: #0b0b0b;
    --paper-light: #ffffff;
    --paper-edge: #d4d4d4;
    --frame: #bdbdbd;
  }
  html, body {
    margin: 0;
    padding: 0;
    overflow: hidden;
  }
  .board {
    position: relative;
    width: 847px;
    height: 1200px;
    box-sizing: border-box;
    border: 2px solid var(--frame);
    border-radius: 8px;
    background: radial-gradient(ellipse at 50% 40%, var(--paper-light) 0%, #eeeeee 55%, var(--paper-edge) 100%);
    overflow: hidden;
    font-family: "Questrial", sans-serif;
  }
  .card {
    position: absolute;
    left: 170px;
    width: 506px;
    height: 289px;
    overflow: hidden;
  }
  .card-front {
    top: 89px;
    background: var(--ink);
    color: var(--brand-blue);
    text-align: center;
  }
  .branch-list {
    margin: 12px 0 0;
    font-size: 15px;
    line-height: 19px;
  }
  .brand-name {
    margin: 70px 0 0;
    font-size: 36px;
    line-height: 1;
    color: var(--brand-blue);
  }
  .tagline {
    margin: 12px 0 0;
    font-size: 20px;
    line-height: 1.1;
    color: var(--brand-blue);
  }
  .website {
    position: absolute;
    bottom: 10px;
    left: 0;
    right: 0;
    margin: 0;
    font-size: 13px;
  }
  .card-back {
    top: 431px;
    color: var(--ink);
  }
  .card-back .backdrop {
    position: absolute;
    inset: 0;
  }
  .contact-name {
    position: absolute;
    top: 12px;
    left: 0;
    width: 452px;
    margin: 0;
    text-align: center;
    font-family: "Tinos", serif;
    font-weight: 700;
    font-size: 33px;
    line-height: 1;
  }
  .name-rule {
    position: absolute;
    top: 49px;
    left: 102px;
    width: 248px;
    height: 2px;
    background: var(--ink);
  }
  .contact-role {
    position: absolute;
    top: 58px;
    left: 0;
    width: 452px;
    margin: 0;
    text-align: center;
    font-size: 15px;
    color: #f4f8fb;
  }
  .contact-details {
    position: absolute;
    top: 97px;
    left: 10px;
    margin: 0;
    font-size: 20px;
    line-height: 25px;
  }
  .contact-details span { display: block; }
  .contact-details .gap { margin-top: 3px; }
  .corner-brand {
    position: absolute;
    right: 14px;
    bottom: 22px;
    font-size: 14px;
    color: var(--brand-blue);
  }
  .brand-showcase {
    position: absolute;
    left: 0;
    right: 0;
    top: 930px;
    text-align: center;
    color: var(--brand-blue);
  }
  .showcase-name {
    margin: 0;
    font-size: 60px;
    line-height: 1;
  }
  .showcase-tagline {
    margin: 18px 0 0;
    font-size: 34px;
    line-height: 1;
  }
</style>
</head>
<body>
<main class="board">

  <section class="card card-front" aria-label="Business card front">
    <p class="branch-list">New York &nbsp;•&nbsp; Savannah &nbsp;•&nbsp; Miami<br>Houston &nbsp;•&nbsp; Los Angeles &nbsp;•&nbsp; Seattle</p>
    <p class="brand-name">Larkwell Shipping</p>
    <p class="tagline">carrying cargo overseas</p>
    <p class="website">www.larkwellgroup.com</p>
  </section>

  <section class="card card-back" aria-label="Business card back">
    <svg class="backdrop" width="506" height="289" viewBox="0 0 506 289" aria-hidden="true">
      <rect width="506" height="289" fill="var(--ink)"/>
      <path d="M0 0 H480 C470 150 330 262 0 289 Z" fill="var(--navy)"/>
      <path d="M0 0 H462 C448 140 310 246 0 272 Z" fill="var(--card-blue)"/>
    </svg>
    <h1 class="contact-name">Tobias Renner</h1>
    <div class="name-rule"></div>
    <p class="contact-role">Chief Operating Officer</p>
    <p class="contact-details">
      <span>2240 Harbor Lane Unit 4b</span>
      <span>Fairmont, NJ 07120</span>
      <span>Direct Extension # 1-718-555-0142</span>
      <span>E-mail Tobias@Larkwellgroup.com</span>
      <span class="gap">Mobile 1-212-555-0187</span>
    </p>
    <span class="corner-brand">Larkwell</span>
  </section>

  <section class="brand-showcase" aria-label="Larkwell Shipping name">
    <p class="showcase-name">Larkwell Shipping</p>
    <p class="showcase-tagline">carrying cargo overseas</p>
  </section>

</main>
</body>
</html>
```